Revamp Existing Business Card Into a Modern Clean Design

See ATTACHED detailed instructions on design, color and business card examples shown to point you into the right direction.

Good luck and May The Force Be With You. :D

```html
<!DOCTYPE html>
<html lang="en">
<head>
<meta charset="utf-8">
<title>Mobile Ridgeway Notary – Business Card</title>
<link href="https://fonts.googleapis.com/css2?family=Varela+Round&family=Oswald:wght@500&display=swap" rel="stylesheet">
<style>
  :root {
    --blue: #2a63b0;
    --blue-deep: #1b4a92;
    --blue-light: #4f86cf;
    --ink: #1f4f97;
    --paper: #f7f9fc;
    --paper-shade: #e4ebf4;
    --backdrop: #e6e8ec;
    --white: #ffffff;
  }
  * { box-sizing: border-box; margin: 0; padding: 0; }
  html, body { width: 1200px; height: 851px; overflow: hidden; background: var(--backdrop); }
  body { position: relative; font-family: "Varela Round", sans-serif; }

  .card {
    position: absolute; top: 19px; width: 480px; height: 813px;
    border-radius: 26px; overflow: hidden;
    box-shadow: 0 6px 18px rgba(0,0,0,0.18);
  }
  .card-front { left: 96px; background: linear-gradient(180deg, var(--paper), var(--paper-shade)); }
  .card-back { left: 608px; background: linear-gradient(160deg, var(--blue-deep), var(--blue) 45%, var(--blue-light)); }

  .shapes { position: absolute; inset: 0; width: 100%; height: 100%; }

  /* Front */
  .brand { position: absolute; right: 70px; top: 64px; text-align: right; color: var(--blue); }
  .brand-name { font-size: 27px; line-height: 1.05; }
  .brand-url { font-size: 9px; margin-top: 3px; color: var(--blue-deep); }
  .brand-mark { position: absolute; right: 28px; top: 46px; width: 38px; height: 38px; border-radius: 50%; background: var(--blue); }

  .contacts { position: absolute; left: 32px; top: 160px; list-style: none; }
  .contacts li { display: flex; align-items: center; height: 29.3px; font-size: 18.5px; color: var(--ink); }
  .contacts li.address { height: auto; align-items: flex-start; }
  .contacts .icon { flex: none; width: 24px; height: 24px; margin-right: 14px; }
  .contacts .address .icon { margin-top: 3px; }
  .contacts .address .lines { line-height: 29.3px; }

  .accept { position: absolute; right: 34px; top: 536px; text-align: right; color: var(--ink); }
  .accept-title { font-size: 21px; }
  .accept-list { font-size: 15.5px; line-height: 1.35; margin-top: 4px; text-transform: uppercase; }

  .payments { position: absolute; left: 34px; top: 624px; display: grid; grid-template-columns: repeat(4, 66px); column-gap: 49px; row-gap: 33px; }
  .pay-badge {
    height: 43px; border-radius: 7px; background: var(--blue);
    color: var(--white); font-size: 13px; white-space: nowrap;
    display: flex; align-items: center; justify-content: center;
    box-shadow: 0 2px 3px rgba(0,0,0,0.25);
  }

  /* Back */
  .intro { position: absolute; left: 20px; right: 18px; top: 14px; color: var(--white); font-size: 19px; line-height: 1.3; }
  .map-area { position: absolute; left: 160px; top: 150px; width: 300px; height: 280px; border-radius: 40%; background: radial-gradient(ellipse at center, rgba(255,255,255,0.2), rgba(255,255,255,0) 70%); }

  .services { position: absolute; left: 22px; top: 110px; list-style: none; width: 450px; }
  .services li { display: flex; align-items: flex-start; color: var(--white); font-size: 17px; line-height: 37.4px; }
  .service-icon { flex: none; width: 62px; height: 33px; margin: 2px 24px 0 0; border-radius: 50%; background: var(--white); display: flex; align-items: center; justify-content: center; }
  .service-icon span { width: 18px; height: 18px; border-radius: 50%; border: 3px solid var(--blue); }

  .clients { position: absolute; inset: 0; color: var(--blue-deep); }
  .client { position: absolute; white-space: nowrap; display: flex; align-items: center; gap: 6px; }
  .client .dot { width: 22px; height: 22px; border-radius: 50%; background: var(--blue-deep); }
  .client .square { width: 32px; height: 32px; background: var(--blue-deep); }

  .clients-label {
    position: absolute; right: 16px; top: 606px;
    font-family: "Oswald", sans-serif; font-weight: 500; color: var(--white);
    font-size: 27px; line-height: 41px; text-transform: uppercase; white-space: nowrap;
  }
  .clients-label .arrow { display: inline-block; width: 0; height: 0; border-top: 12px solid transparent; border-bottom: 12px solid transparent; border-right: 20px solid var(--white); margin-right: 14px; vertical-align: -2px; }
  .label-line { display: block; text-align: right; }
</style>
</head>
<body>

<section class="card card-front" aria-label="Business card front">
  <svg class="shapes" viewBox="0 0 480 813" preserveAspectRatio="none" aria-hidden="true">
    <defs>
      <linearGradient id="frontWave" x1="0" y1="0" x2="1" y2="1">
        <stop offset="0" stop-color="#1b4a92"/>
        <stop offset="1" stop-color="#4f86cf"/>
      </linearGradient>
    </defs>
    <path d="M0 0 H190 C120 30 50 80 0 170 Z" fill="url(#frontWave)"/>
    <path d="M0 0 H240 C150 20 60 70 0 140 Z" fill="#4f86cf" opacity="0.35"/>
    <path d="M0 500 C150 490 330 470 480 400 V495 C330 500 160 530 0 575 Z" fill="url(#frontWave)"/>
    <path d="M0 575 C160 530 330 500 480 495 V512 C330 518 170 548 0 592 Z" fill="#4f86cf" opacity="0.35"/>
    <path d="M0 790 C160 780 320 780 480 788 V813 H0 Z" fill="url(#frontWave)"/>
  </svg>

  <span class="brand-mark"></span>
  <div class="brand">
    <div class="brand-name">Mobile Ridgeway<br>Notary</div>
    <div class="brand-url">www.ridgewaynotary.com</div>
  </div>

  <ul class="contacts">
    <li><svg class="icon" viewBox="0 0 24 24"><circle cx="12" cy="12" r="12" fill="#2a63b0"/><path d="M8.5 6.5l2 2-1.2 1.6c.7 1.6 2 2.9 3.6 3.6l1.6-1.2 2 2-1.4 1.8c-3.8-.6-7.4-4.2-8-8z" fill="#fff"/></svg>555-010-2500</li>
    <li><svg class="icon" viewBox="0 0 24 24"><circle cx="12" cy="12" r="12" fill="#2a63b0"/><rect x="8" y="6" width="8" height="5" fill="#fff"/><rect x="6" y="11" width="12" height="6" rx="1" fill="#fff"/></svg>555-010-53-56</li>
    <li><svg class="icon" viewBox="0 0 24 24"><circle cx="12" cy="12" r="12" fill="#2a63b0"/><circle cx="12" cy="12" r="6" fill="none" stroke="#fff" stroke-width="1.5"/><path d="M6 12h12M12 6v12" stroke="#fff" stroke-width="1.3"/></svg>www.ridgewaynotary.com</li>
    <li><svg class="icon" viewBox="0 0 24 24"><circle cx="12" cy="12" r="12" fill="#2a63b0"/><rect x="6" y="8" width="12" height="8" fill="#fff"/><path d="M6 8l6 5 6-5" fill="none" stroke="#2a63b0" stroke-width="1.3"/></svg>hello@ridgewaynotary.com</li>
    <li><svg class="icon" viewBox="0 0 24 24"><circle cx="12" cy="12" r="12" fill="#2a63b0"/></svg>www.chirpline.com/ridgewaynotary</li>
    <li><svg class="icon" viewBox="0 0 24 24"><circle cx="12" cy="12" r="12" fill="#2a63b0"/></svg>www.viewtube.com/ridgewaynotary</li>
    <li><svg class="icon" viewBox="0 0 24 24"><circle cx="12" cy="12" r="12" fill="#2a63b0"/></svg>www.pinboard.com/ridgewaynotary</li>
    <li><svg class="icon" viewBox="0 0 24 24"><circle cx="12" cy="12" r="12" fill="#2a63b0"/></svg>www.friendsbook.com/ridgewaynotary</li>
    <li class="address"><svg class="icon" viewBox="0 0 24 24"><circle cx="12" cy="12" r="12" fill="#2a63b0"/><path d="M12 5a4.5 4.5 0 0 0-4.5 4.5C7.5 13 12 19 12 19s4.5-6 4.5-9.5A4.5 4.5 0 0 0 12 5z" fill="#fff"/><circle cx="12" cy="9.5" r="1.7" fill="#2a63b0"/></svg><span class="lines">4200 Cedar Ridge Blvd<br>Ste 118-240 Ridgeway,<br>TX 78000</span></li>
  </ul>

  <div class="accept">
    <div class="accept-title">We accept:</div>
    <div class="accept-list">Cash, checks, Paylink and all<br>major credit and debit cards</div>
  </div>

  <div class="payments">
    <div class="pay-badge">Vexa</div>
    <div class="pay-badge">Meridian</div>
    <div class="pay-badge">Farpoint</div>
    <div class="pay-badge">Atlas Pay</div>
    <div class="pay-badge">Paylink</div>
    <div class="pay-badge">Debit</div>
    <div class="pay-badge">Check</div>
    <div class="pay-badge">Cash</div>
  </div>
</section>

<section class="card card-back" aria-label="Business card back">
  <div class="map-area" role="img" aria-label="Faint state map outline in light blue"></div>

  <p class="intro">Mobile Ridgeway Notary provides these mobile legal real estate service to companies and the general public around the world:</p>

  <ul class="services">
    <li><span class="service-icon"><span></span></span>Texas process serving services</li>
    <li><span class="service-icon"><span></span></span>Texas loan signing agent services</li>
    <li><span class="service-icon"><span></span></span>Texas mobile notary public services</li>
    <li><span class="service-icon"><span></span></span><span>Texas Secretary of State rush apostille &amp;<br>authentication services</span></li>
    <li><span class="service-icon"><span></span></span><span>U.S Department of State rush apostille &amp;<br>authentication services</span></li>
    <li><span class="service-icon"><span></span></span><span>U.S Embassy or Consulate rush document<br>legalization services</span></li>
  </ul>

  <svg class="shapes" viewBox="0 0 480 813" preserveAspectRatio="none" aria-hidden="true">
    <path d="M0 462 H190 C270 475 320 540 312 620 C305 690 260 730 250 782 H0 Z" fill="#f7f9fc"/>
    <path d="M0 786 H480 V813 H0 Z" fill="#1b4a92"/>
    <path d="M0 790 H480" stroke="#ffffff" stroke-width="2" opacity="0.8"/>
  </svg>

  <div class="clients">
    <div class="client" style="left:16px;top:476px;font-size:19px;">Harlow Finch</div>
    <div class="client" style="left:12px;top:516px;font-size:19px;line-height:1;">Greenfield<br>Market</div>
    <div class="client" style="left:128px;top:556px;font-size:15px;">Westbrook Bank</div>
    <div class="client" style="left:12px;top:590px;font-size:14px;line-height:1.1;"><span class="square"></span>Crestline<br>Fuel</div>
    <div class="client" style="left:108px;top:594px;font-size:22px;">Corvane Energy</div>
    <div class="client" style="left:90px;top:638px;font-size:18px;">Kessler Trust</div>
    <div class="client" style="left:13px;top:676px;font-size:30px;"><span class="dot"></span>Shopforge</div>
    <div class="client" style="left:18px;top:728px;font-size:38px;">Civica Bank</div>
  </div>

  <div class="clients-label">
    <span class="label-line"><span class="arrow"></span>Some of</span>
    <span class="label-line">our local &amp;</span>
    <span class="label-line">national</span>
    <span class="label-line">clients</span>
  </div>
</section>

</body>
</html>
```